I would like to purchase a customized version of a design you have previously submitted - https://www.artvaultly.com/design/58314720
hi
would like the design about the some. just with our  details and logo
office number 01563829140
Mobil number 07812645037
web sparlowcleaning.ltd
email sparlowcleaning@mailtrove.co.uk
on the back we would like to put a price list

```html
<!DOCTYPE html>
<html lang="en">
<head>
<meta charset="utf-8">
<title>Sparlow Cleaning &amp; Maintenance – Flyer, front and back</title>
<link rel="stylesheet" href="https://fonts.googleapis.com/css2?family=Poppins:wght@400;500;600;700;800&family=Francois+One&display=swap">
<style>
  :root{
    --navy:#1f2a8c;
    --royal:#2e3fb0;
    --sky:#3f8fd8;
    --brand:#2f6fc9;
    --ink:#111111;
    --grey:#9aa5b1;
    --grey-light:#dfe4ec;
    --white:#ffffff;
    --row-1:#2a3594;
    --row-2:#1f6ab3;
    --row-3:#3f86cc;
    --row-4:#58ade0;
    --row-5:#8ac3e6;
  }
  *{box-sizing:border-box;margin:0;padding:0}
  html,body{width:815px;height:1200px;overflow:hidden;background:var(--white)}
  body{font-family:"Poppins",sans-serif;color:var(--ink);position:relative}

  .page{position:absolute;top:312px;width:815px;height:1200px;overflow:hidden;background:var(--white);
    transform:scale(.48);transform-origin:0 0}
  .page-front{left:11px}
  .page-back{left:413px}
  .artwork{position:absolute;inset:0;width:815px;height:1200px}
  .abs{position:absolute}

  /* front */
  .brand{left:37px;top:30px}
  .brand-name{font-weight:800;font-size:70px;line-height:1;color:var(--brand);letter-spacing:-2px}
  .brand-sub{font-weight:400;font-size:19px;color:var(--brand);margin-top:6px;letter-spacing:-.2px}

  .headline{left:37px;top:538px;width:320px}
  .headline .l1{font-weight:800;font-size:56px;line-height:1;letter-spacing:1px}
  .headline .l2{font-family:"Francois One",sans-serif;font-weight:400;font-size:37px;line-height:1.05;color:var(--navy);margin-top:6px;letter-spacing:.5px}
  .headline .l3{font-weight:800;font-size:60px;line-height:1}

  .audience{left:0;top:717px;width:353px;height:58px;background:var(--grey);color:var(--white);
    font-weight:600;font-size:14px;line-height:1.05;padding:11px 0 0 37px}

  .quote{left:37px;top:793px}
  .quote .q1{font-weight:700;font-size:26px;color:var(--sky);line-height:1.05}
  .quote .q2{font-weight:700;font-size:23px;line-height:1.1}

  .contacts{left:37px;top:861px;list-style:none}
  .contacts li{display:flex;align-items:center;gap:12px;height:27.5px;font-weight:600;font-size:15px}
  .contacts svg{width:15px;height:15px;flex:none}

  .social{left:37px;top:977px}
  .social .label{font-weight:600;font-size:15px;color:var(--navy)}
  .social .dots{display:flex;gap:10px;margin-top:10px}
  .social .dots span{width:24px;height:24px;border-radius:5px;background:var(--navy)}
  .social .handle{font-weight:600;font-size:13px;color:var(--navy);margin-top:6px}

  .tab{background:var(--white);color:var(--grey);font-weight:700;font-size:20px;line-height:30px;
    padding-left:20px;border-radius:0 6px 6px 0;letter-spacing:.5px}
  .tab-about{left:402px;top:594px;width:171px}
  .tab-services{left:377px;top:733px;width:196px}

  .about{left:402px;top:636px;width:360px;color:var(--white)}
  .about h3{font-weight:600;font-size:10px}
  .about p{font-size:10px;line-height:1.28;margin-top:3px}

  .service{width:150px;text-align:center;color:var(--white);font-weight:600;font-size:12.5px;line-height:1.25}
  .service svg{display:block;margin:0 auto 6px;width:40px;height:40px}

  .promise{left:380px;top:978px;width:420px;color:var(--white);font-weight:700;font-size:16.5px;line-height:1.32}

  .cta{left:0;top:1088px;width:815px;text-align:center;color:var(--white)}
  .cta .c1{font-weight:600;font-size:21px;color:var(--sky)}
  .cta .c2{font-size:19px;line-height:1.3}

  /* back */
  .price-title{left:0;top:24px;width:815px;text-align:center;color:var(--white);font-weight:800;font-size:47px;letter-spacing:1px}
  .section-title{left:0;width:815px;text-align:center;color:var(--sky);font-weight:700;font-size:23px;letter-spacing:2px}
  .st-window{top:298px}
  .st-other{top:836px}

  .tier{left:37px;width:440px;height:95px;display:flex;align-items:center;justify-content:center;
    color:var(--white);font-weight:600;font-size:20px;border-radius:2px}
  .tier-prices{left:486px;width:293px;list-style:none}
  .tier-prices li{height:22.5px;margin-bottom:1px;background:var(--grey-light);text-align:center;font-size:12.5px;line-height:22.5px}
  .tier-prices li.head{height:27px;line-height:27px;background:var(--ink);color:var(--white);font-weight:600;font-size:14px;border-radius:2px}

  .extra{width:208px}
  .extra .card{height:81px;background:#a3adb9;border-radius:2px;text-align:center;padding-top:18px;color:var(--white);font-weight:600;font-size:14px;line-height:1.05}
  .extra .card .from{color:var(--navy);font-weight:700;font-size:12px;margin-top:4px}
  .extra .line{height:24px;margin-top:6px;background:var(--grey-light);text-align:center;font-size:12px;line-height:24px;border-radius:2px}
</style>
</head>
<body>

<!-- Front -->
<main class="page page-front">
  <svg class="artwork" viewBox="0 0 815 1200" xmlns="http://www.w3.org/2000/svg">
    <defs>
      <linearGradient id="photoTone" x1="0" y1="0" x2="1" y2="1">
        <stop offset="0" stop-color="#6b6f74"/>
        <stop offset=".35" stop-color="#e8e2d6"/>
        <stop offset=".7" stop-color="#c9cdd3"/>
        <stop offset="1" stop-color="#8aa0b8"/>
      </linearGradient>
      <linearGradient id="panel" x1="0" y1="0" x2="0" y2="1">
        <stop offset="0" stop-color="#3448bd"/>
        <stop offset="1" stop-color="#1c2684"/>
      </linearGradient>
      <linearGradient id="greyBand" x1="0" y1="0" x2="1" y2="0">
        <stop offset="0" stop-color="#8e99a6"/>
        <stop offset="1" stop-color="#dfe4ea"/>
      </linearGradient>
      <linearGradient id="gutterTone" x1="0" y1="0" x2="1" y2="1">
        <stop offset="0" stop-color="#7d8a8f"/>
        <stop offset=".6" stop-color="#4a3b2c"/>
        <stop offset="1" stop-color="#d9d2c6"/>
      </linearGradient>
      <linearGradient id="glassTone" x1="0" y1="0" x2="1" y2="1">
        <stop offset="0" stop-color="#e9eef3"/>
        <stop offset=".5" stop-color="#9fb3c4"/>
        <stop offset="1" stop-color="#e3c84a"/>
      </linearGradient>
    </defs>
    <path role="img" aria-label="Photo of a window cleaner clearing a house gutter"
      d="M0,178 C220,165 430,110 530,0 L815,0 L815,560 L380,560 C250,530 120,480 0,430 Z" fill="url(#photoTone)"/>
    <path d="M0,150 C220,140 420,90 505,0 L548,0 C440,125 230,178 0,190 Z" fill="var(--navy)"/>
    <path d="M470,0 C440,40 410,70 380,90 C430,60 470,30 500,0 Z" fill="var(--sky)"/>
    <path d="M0,425 C120,475 250,520 400,545 L400,565 C250,548 110,505 0,462 Z" fill="url(#greyBand)"/>
    <path d="M0,462 C110,505 250,548 400,565 L400,720 L0,720 Z" fill="var(--white)"/>
    <path d="M353,1130 L353,620 C353,565 380,535 425,515 C545,465 690,440 815,330 L815,1130 Z" fill="url(#panel)"/>
    <circle cx="482" cy="470" r="96" fill="#c4ccd6"/>
    <circle role="img" aria-label="Photo of a gloved hand scooping leaves from a gutter" cx="482" cy="470" r="89" fill="url(#gutterTone)"/>
    <circle cx="665" cy="440" r="121" fill="#c4ccd6"/>
    <circle role="img" aria-label="Photo of a gloved hand wiping a window with a cloth and spray bottle" cx="665" cy="440" r="113" fill="url(#glassTone)"/>
    <path d="M0,1080 C200,1052 560,1042 815,1072 L815,1200 L0,1200 Z" fill="url(#greyBand)"/>
    <path d="M0,1097 C200,1072 560,1064 815,1090 L815,1200 L0,1200 Z" fill="var(--ink)"/>
  </svg>

  <header class="abs brand">
    <div class="brand-name">SPARLOW</div>
    <div class="brand-sub">CLEANING &amp; MAINTENANCE LTD</div>
  </header>

  <h1 class="abs headline">
    <div class="l1">RELIABLE</div>
    <div class="l2">WINDOW CLEANING</div>
    <div class="l3">SERVICES</div>
  </h1>

  <div class="abs audience">FOR RESIDENTIAL AND COMMERCIAL<br>CUSTOMERS IN AND AROUND ESSEX.</div>

  <div class="abs quote">
    <div class="q1">FOR A FREE QUOTE</div>
    <div class="q2">PLEASE CONTACT US</div>
  </div>

  <ul class="abs contacts">
    <li><svg viewBox="0 0 16 16"><rect x="2" y="6" width="12" height="8" rx="1" fill="var(--brand)"/><path d="M1,6 C3,1 13,1 15,6 L12,6 L11,4 L5,4 L4,6 Z" fill="var(--brand)"/></svg>01563829140</li>
    <li><svg viewBox="0 0 16 16"><path d="M3,1 L6,1 L7,5 L5,6.5 C6,9 7,10 9.5,11 L11,9 L15,10 L15,13 C15,14 14,15 13,15 C7,15 1,9 1,3 C1,2 2,1 3,1 Z" fill="var(--brand)"/></svg>07812645037</li>
    <li><svg viewBox="0 0 16 16"><rect x="1" y="3" width="14" height="10" rx="1" fill="var(--brand)"/><path d="M1.5,3.5 L8,9 L14.5,3.5" stroke="#fff" stroke-width="1.3" fill="none"/></svg>sparlowcleaning@mailtrove.co.uk</li>
    <li><svg viewBox="0 0 16 16"><circle cx="8" cy="8" r="6.5" fill="none" stroke="var(--brand)" stroke-width="1.5"/><path d="M1.5,8 H14.5 M8,1.5 C4.5,5 4.5,11 8,14.5 M8,1.5 C11.5,5 11.5,11 8,14.5" stroke="var(--brand)" stroke-width="1.2" fill="none"/></svg>www.sparlowcleaning.ltd</li>
  </ul>

  <div class="abs social">
    <div class="label">FOLLOW US ON SOCIAL MEDIA</div>
    <div class="dots"><span></span><span></span><span></span></div>
    <div class="handle">@SparlowCleaning&amp;MaintenanceLTD</div>
  </div>

  <div class="abs tab tab-about">ABOUT US</div>
  <div class="abs about">
    <h3>RESIDENTIAL AND COMMERCIAL WINDOW CLEANING IN ESSEX.</h3>
    <p>Window Cleaning EssexSparlow Cleaning Ltd have been cleaning windows for commercial and residential properties throughout Hutton, Shenfield and the surrounding areas since 1999. We cover most towns in Essex including Brentwood, Chelmsford, Romford, Loughton and Billericay.</p>
  </div>

  <div class="abs tab tab-services">OUR SERVICES</div>

  <div class="abs service" style="left:344px;top:775px">
    <svg viewBox="0 0 40 40"><circle cx="20" cy="20" r="17" fill="none" stroke="#fff" stroke-width="1.5"/><circle cx="20" cy="20" r="12" fill="none" stroke="#fff" stroke-width="1"/><rect x="14" y="13" width="12" height="14" fill="none" stroke="#fff" stroke-width="1.5"/><path d="M20,13 V27 M14,20 H26" stroke="#fff" stroke-width="1.2"/></svg>
    WINDOW<br>CLEANING
  </div>
  <div class="abs service" style="left:488px;top:775px">
    <svg viewBox="0 0 40 40"><circle cx="20" cy="20" r="17" fill="none" stroke="#fff" stroke-width="1.5"/><circle cx="20" cy="20" r="12" fill="none" stroke="#fff" stroke-width="1"/><path d="M13,27 V19 L20,13 L27,19 V27 Z" fill="none" stroke="#fff" stroke-width="1.5"/><path d="M17,27 V22 H23 V27" stroke="#fff" stroke-width="1.2" fill="none"/></svg>
    CONSERVATORY<br>CLEANING
  </div>
  <div class="abs service" style="left:642px;top:775px">
    <svg viewBox="0 0 40 40"><circle cx="20" cy="20" r="17" fill="none" stroke="#fff" stroke-width="1.5"/><circle cx="20" cy="20" r="12" fill="none" stroke="#fff" stroke-width="1"/><path d="M13,24 H21 L25,18 H28 M21,24 V28 H15 V24" stroke="#fff" stroke-width="1.5" fill="none"/><path d="M29,15 L31,13 M29,18 H32 M29,21 L31,23" stroke="#fff" stroke-width="1.2"/></svg>
    PRESSURE<br>WASHING
  </div>
  <div class="abs service" style="left:414px;top:864px">
    <svg viewBox="0 0 40 40"><circle cx="20" cy="20" r="17" fill="none" stroke="#fff" stroke-width="1.5"/><circle cx="20" cy="20" r="12" fill="none" stroke="#fff" stroke-width="1"/><path d="M13,15 H27 V19 C27,22 24,24 20,24 C16,24 13,22 13,19 Z" fill="none" stroke="#fff" stroke-width="1.5"/><path d="M20,24 V29" stroke="#fff" stroke-width="1.5"/></svg>
    GUTTER<br>CLEANING
  </div>
  <div class="abs service" style="left:565px;top:864px">
    <svg viewBox="0 0 40 40"><circle cx="20" cy="20" r="17" fill="none" stroke="#fff" stroke-width="1.5"/><circle cx="20" cy="20" r="12" fill="none" stroke="#fff" stroke-width="1"/><path d="M12,22 L20,14 L28,22 M14,22 H26 V27 H14 Z" fill="none" stroke="#fff" stroke-width="1.5"/></svg>
    SOFFIT'S &amp; FASCIA<br>CLEANING
  </div>

  <p class="abs promise">WE ARE HAPPY TO PROVIDE FREE, FRIENDLY ADVICE AND AN ON SITE DEMONSTRATION OF OUR WINDOW CLEANING CAPABILITIES.</p>

  <footer class="abs cta">
    <div class="c1">USE ‘CONTACT US’ FORM</div>
    <div class="c2">on our web site &amp; add images of your property,<br>we will then provide a quote with-in 48 Hours.</div>
  </footer>
</main>

<!-- Back: price list -->
<section class="page page-back">
  <svg class="artwork" viewBox="0 0 815 1200" xmlns="http://www.w3.org/2000/svg">
    <defs>
      <linearGradient id="backBand" x1="0" y1="0" x2="0" y2="1">
        <stop offset="0" stop-color="#2336a6"/>
        <stop offset="1" stop-color="#1c2684"/>
      </linearGradient>
      <linearGradient id="backGrey" x1="0" y1="0" x2="1" y2="0">
        <stop offset="0" stop-color="#8e99a6"/>
        <stop offset="1" stop-color="#dfe4ea"/>
      </linearGradient>
      <linearGradient id="officeTone" x1="0" y1="0" x2="0" y2="1">
        <stop offset="0" stop-color="#7d5a4a"/>
        <stop offset=".6" stop-color="#a8a39c"/>
        <stop offset="1" stop-color="#d8dadd"/>
      </linearGradient>
      <linearGradient id="houseTone" x1="0" y1="0" x2="0" y2="1">
        <stop offset="0" stop-color="#7fb2e0"/>
        <stop offset=".55" stop-color="#8c5a44"/>
        <stop offset="1" stop-color="#4f8a2e"/>
      </linearGradient>
      <linearGradient id="roofTone" x1="0" y1="0" x2="0" y2="1">
        <stop offset="0" stop-color="#e6e8ea"/>
        <stop offset=".55" stop-color="#b34a44"/>
        <stop offset="1" stop-color="#d5d9de"/>
      </linearGradient>
    </defs>
    <path d="M0,0 H815 V140 C700,160 620,210 407,212 C195,210 115,160 0,140 Z" fill="url(#backBand)"/>
    <path d="M15,128 C110,170 210,205 320,218 L320,230 C200,220 100,190 15,128 Z" fill="url(#backGrey)"/>
    <path d="M800,128 C705,170 605,205 495,218 L495,230 C615,220 715,190 800,128 Z" fill="url(#backGrey)"/>
    <circle cx="186" cy="183" r="92" fill="#c4ccd6"/>
    <circle role="img" aria-label="Photo of an office building with a cleaning van outside" cx="186" cy="183" r="85" fill="url(#officeTone)"/>
    <circle cx="397" cy="183" r="92" fill="#c4ccd6"/>
    <circle role="img" aria-label="Photo of a brick house with a green lawn being cleaned" cx="397" cy="183" r="85" fill="url(#houseTone)"/>
    <circle cx="607" cy="183" r="92" fill="#c4ccd6"/>
    <circle role="img" aria-label="Photo of a white conservatory with a red tiled roof" cx="607" cy="183" r="85" fill="url(#roofTone)"/>
    <path d="M0,1080 C200,1052 560,1042 815,1072 L815,1200 L0,1200 Z" fill="url(#backGrey)"/>
    <path d="M0,1097 C200,1072 560,1064 815,1090 L815,1200 L0,1200 Z" fill="var(--ink)"/>
  </svg>

  <h2 class="abs price-title">OUR PRODUCT PRICE LIST</h2>

  <h3 class="abs section-title st-window">RELIABLE WINDOW CLEANING SERVICE PRICES</h3>

  <div class="abs tier" style="top:333px;background:var(--row-1)">SEMI DETACHED (3/4 BED)</div>
  <ul class="abs tier-prices" style="top:331px">
    <li class="head">From £14 per visit</li>
    <li>+ Conservatory roofs from £60.00</li>
    <li>+ Drives from £120.00</li>
    <li>+ Gutters from £60.00</li>
  </ul>

  <div class="abs tier" style="top:433px;background:var(--row-2)">DETACHED (3/4 BED)</div>
  <ul class="abs tier-prices" style="top:431px">
    <li class="head">From £16 per visit</li>
    <li>+ Conservatory roofs from £60.00</li>
    <li>+ Drives from £120.00</li>
    <li>+ Gutters from £60.00</li>
  </ul>

  <div class="abs tier" style="top:533px;background:var(--row-3)">DETACHED (5 BED)</div>
  <ul class="abs tier-prices" style="top:531px">
    <li class="head">From £23 per visit</li>
    <li>+ Conservatory roofs from £60.00</li>
    <li>+ Drives from £120.00</li>
    <li>+ Gutters from £60.00</li>
  </ul>

  <div class="abs tier" style="top:633px;background:var(--row-4)">TERRACE (FRONT ONLY)</div>
  <ul class="abs tier-prices" style="top:631px">
    <li class="head">From £10 per visit</li>
    <li>+ Conservatory roofs from £60.00</li>
    <li>+ Drives from £120.00</li>
    <li>+ Gutters from £60.00</li>
  </ul>

  <div class="abs tier" style="top:733px;background:var(--row-5)">TERRACE (FRONT AND BACK)</div>
  <ul class="abs tier-prices" style="top:731px">
    <li class="head">FROM £14 PER VISIT</li>
    <li>+ Conservatory roofs from £60.00</li>
    <li>+ Drives from £120.00</li>
    <li>+ Gutters from £60.00</li>
  </ul>

  <h3 class="abs section-title st-other">OTHER CLEANING SERVICES</h3>

  <div class="abs extra" style="left:56px;top:872px">
    <div class="card">CONSERVATORY ROOF<br>CLEANING<div class="from">FROM £60 PER VISIT</div></div>
    <div class="line">+ Drives from £120.00</div>
    <div class="line">+ Gutters from £60.00</div>
  </div>
  <div class="abs extra" style="left:315px;top:872px">
    <div class="card">DRIVEWAYS &amp; PATIO<br>CLEANING<div class="from">FROM £120 PER VISIT</div></div>
    <div class="line">+ Conservatory roofs from £60.00</div>
    <div class="line">+ Gutters from £60.00</div>
  </div>
  <div class="abs extra" style="left:566px;top:872px">
    <div class="card" style="padding-top:25px">GUTTER CLEANING<div class="from" style="margin-top:12px">FROM £120 PER VISIT</div></div>
    <div class="line">+ Conservatory roofs from £60.00</div>
    <div class="line">+ Drives from £120.00</div>
  </div>

  <footer class="abs cta">
    <div class="c1">USE ‘CONTACT US’ FORM</div>
    <div class="c2">on our web site &amp; add images of your property,<br>we will then provide a quote with-in 48 Hours.</div>
  </footer>
</section>

</body>
</html>
```